KTR Motorhaus Automotive Repair and Service Shop

I need an informative and interactive website for my automotive service and repair shop. The website must give information about the shop, as well as the ability to make bookings and a forums page for our users to use and set up an account with us, in which we can give promotions via email. We are located in Pompano Beach Florida and our company name is KTR Motorhaus. Our color scheme is a red for accent and grey (neutral color) as a base. The design must communicate our message and be able to grow should we decide to retail parts in the future. One of the websites I take the highest inspiration from is http://www.lanvexbodyshop.example/. Although I do not have as nearly as many certifications as them. Attached are some images of our shop so you can see how clean and modern our building is, and I would like our website to match our feel. Thank you.

Target Market(s)

Automotive Enthusiasts

Industry/Entity Type

Automotive

Contact Information for Business Card

KTR Motorhaus /954 718 6402 /rohan@ktrmotorhaus.example/ 512 NE 9th St Pompano Beach FL 33062/ any other info needed please ask me

Coding

Coded - Design and coding required

Number of Pages Required

5+ page

Font styles to use
Sans Serif

Requirements
Must have
• Name, logo, contact info, location, phone number
Nice to have
• Building is very modern, would like a business card to match
Should not have
• Not to playful or vibrant

```html
<!DOCTYPE html>
<html lang="en">
<head>
<meta charset="utf-8">
<title>KTR Motorhaus – Automotive Repair and Service</title>
<link href="https://fonts.googleapis.com/css2?family=Roboto+Condensed:wght@400;700&family=Roboto:wght@400;500;700&display=swap" rel="stylesheet">
<style>
:root{
  --red:#e8323c;
  --ink:#1d1d1f;
  --dark:#222428;
  --darker:#17181a;
  --grey:#6b6d70;
  --line:#dedede;
  --white:#ffffff;
}
*{box-sizing:border-box;margin:0;padding:0}
html,body{width:1200px;height:2484px;overflow:hidden}
body{font-family:"Roboto",Arial,sans-serif;color:var(--ink);background:var(--white);font-size:13px;line-height:1.55}
h1,h2,h3,h4,.brand{font-family:"Roboto Condensed","Arial Narrow",sans-serif}
.wrap{width:1040px;margin:0 auto;position:relative}

.topbar{height:56px;background:var(--white)}
.topbar .wrap{display:flex;align-items:center;height:56px}
.brand{font-size:28px;font-weight:700;letter-spacing:.5px;color:var(--ink);white-space:nowrap}
.top-contacts{margin-left:auto;display:flex;gap:26px;align-items:center;font-size:12px;color:var(--grey)}
.top-contacts span{display:flex;align-items:center;gap:8px}
.ico{width:26px;height:26px;border-radius:50%;border:1px solid var(--red);display:inline-flex;align-items:center;justify-content:center}
.btn-cart{width:38px;height:26px;background:var(--red);border-radius:3px;display:inline-flex;align-items:center;justify-content:center}

.nav{height:40px;background:var(--red)}
.nav .wrap{display:flex;align-items:center;height:40px}
.nav a{color:var(--white);text-decoration:none;font-size:12px;font-weight:700;margin-right:30px;letter-spacing:.5px}
.search{margin-left:auto;width:180px;height:24px;background:var(--white);border-radius:2px;display:flex;align-items:center;justify-content:space-between;padding:0 8px;font-size:11px;color:#999}

.hero{height:352px;position:relative;background:linear-gradient(100deg,#3a3c40 0%,#2a2b2e 45%,#151618 100%)}
.hero-text{position:absolute;left:640px;top:176px;width:470px;color:var(--white)}
.hero-text h1{font-size:40px;line-height:1.05;font-weight:700;letter-spacing:.5px;white-space:nowrap}
.hero-text h2{font-size:36px;font-weight:400;line-height:1.1;margin-bottom:10px;white-space:nowrap}
.hero-text p{font-size:12px;width:420px;line-height:1.5;color:#ddd}

.partners{height:112px;display:flex;align-items:center;justify-content:center;gap:86px}
.partner{width:110px;height:28px;background:#cfd0d2;border-radius:3px}

.intro{height:472px;border-top:1px solid var(--line)}
.sec-title{text-align:center;font-size:26px;font-weight:700;letter-spacing:.5px;padding-top:30px;line-height:1.3}
.sec-lead{text-align:center;font-size:12px;color:var(--grey);width:520px;margin:8px auto 0}
.intro-body{display:flex;margin-top:44px;gap:40px}
.intro-photo{width:420px;height:236px;flex:none;background:linear-gradient(135deg,#d9d9db,#b42a31 60%,#6a6a6e);border-bottom:4px solid var(--red)}
.intro-list{flex:1;padding-top:4px}
.intro-list h3{font-size:15px;color:var(--red);margin-bottom:4px}
.intro-list > p{color:var(--grey);font-size:12px;width:440px;margin-bottom:16px}
.feature{display:flex;gap:16px;margin-bottom:16px}
.feature .badge{width:46px;height:46px;background:var(--red);border-radius:4px;flex:none;display:flex;align-items:center;justify-content:center}
.feature h4{font-size:13px;color:var(--red);font-weight:400}
.feature p{font-size:11px;color:var(--grey);width:300px;line-height:1.45}

.services{height:456px;background:linear-gradient(180deg,#2b2c2f,#1c1d1f)}
.services .sec-title{color:var(--white);padding-top:40px}
.services .sec-lead{color:#bbb}
.cards{display:flex;justify-content:center;gap:32px;margin-top:28px}
.card{width:236px}
.card .photo{height:184px}
.card h4{color:var(--white);font-size:16px;margin-top:12px}
.card h4.accent{color:var(--red)}
.card p{color:#bbb;font-size:11px;line-height:1.45}

.split{height:220px;margin-top:12px;background:linear-gradient(90deg,#3a3b3e,#5a5c60 50%,#3d3e41);position:relative}
.split .wrap{display:flex;gap:60px;padding-top:20px}
.split h3{color:var(--white);font-size:22px;font-weight:700;letter-spacing:.5px;margin-bottom:12px}
.split h3::after{content:"";display:block;width:40px;height:3px;background:var(--red);margin-top:6px}
.quote{width:460px;background:var(--white);padding:16px 20px;height:120px;position:relative;font-size:11px;color:var(--grey)}
.quote b{display:block;color:var(--ink);font-size:12px;margin-bottom:4px}
.quote .avatar{position:absolute;right:24px;bottom:-22px;width:56px;height:56px;border:3px solid var(--white);background:linear-gradient(#d4c7bd,#8a7b70)}
.form{width:460px}
.form-row{display:flex;gap:10px;margin-bottom:8px}
.field{flex:1;height:26px;background:var(--white);font-size:10px;color:#999;padding:6px 8px}
.field.tall{height:34px}
.submit{width:92px;height:28px;background:var(--red);color:var(--white);font-size:11px;font-weight:700;display:flex;align-items:center;justify-content:center}

.about{height:352px;text-align:center}
.about .sec-title{padding-top:44px}
.about p{width:920px;margin:16px auto 0;font-size:12px;color:var(--grey);text-align:left}
.btn-dark{display:inline-block;margin-top:28px;background:var(--ink);color:var(--white);font-size:11px;font-weight:700;padding:10px 26px}

.newsletter{height:116px;background:var(--red)}
.newsletter .wrap{display:flex;align-items:center;height:116px}
.nl-title{margin-left:18px;color:var(--white);line-height:1}
.nl-title small{font-size:12px;font-weight:700;letter-spacing:1px;display:block}
.nl-title strong{font-family:"Roboto Condensed",sans-serif;font-size:28px}
.nl-form{margin-left:auto;display:flex;margin-right:40px}
.nl-form .field{width:260px;height:32px;flex:none}
.nl-form .go{width:100px;height:32px;background:var(--ink);color:var(--white);font-size:11px;display:flex;align-items:center;justify-content:center}

.footer{height:284px;background:var(--dark);color:#c9c9c9}
.footer .wrap{display:flex;padding-top:40px}
.f-brand{width:420px;font-size:11px;line-height:1.5}
.f-brand .brand{color:var(--white);font-size:30px;margin-bottom:12px}
.f-brand p{width:250px;margin-bottom:10px}
.f-col{width:200px;font-size:11px}
.f-col h4{color:var(--white);font-size:15px;font-weight:400;margin-bottom:12px}
.f-col li{list-style:none;margin-bottom:5px}
.f-contact{width:260px}
.f-contact li{display:flex;gap:8px;align-items:flex-start;margin-bottom:12px;width:250px}
.f-contact .dot{width:16px;height:16px;border-radius:50%;background:var(--white);flex:none;display:flex;align-items:center;justify-content:center}
.copy{height:24px;background:var(--darker);color:#8a8a8a;font-size:10px;text-align:center;line-height:24px}
</style>
</head>
<body>

<header class="topbar">
  <div class="wrap">
    <div class="brand">KTR MOTORHAUS</div>
    <div class="top-contacts">
      <span><i class="ico"><svg width="12" height="12" viewBox="0 0 24 24"><path fill="#e8323c" d="M6.6 10.8a15 15 0 0 0 6.6 6.6l2.2-2.2c.3-.3.7-.4 1-.2 1.1.4 2.3.6 3.6.6.6 0 1 .4 1 1V20c0 .6-.4 1-1 1A17 17 0 0 1 3 4c0-.6.4-1 1-1h3.5c.6 0 1 .4 1 1 0 1.3.2 2.5.6 3.6.1.3 0 .7-.2 1z"/></svg></i>954 718 6402</span>
      <span><i class="ico"><svg width="12" height="12" viewBox="0 0 24 24"><path fill="#e8323c" d="M3 5h18v14H3zm2 2v.5l7 4.5 7-4.5V7z"/></svg></i>rohan@ktrmotorhaus.example</span>
      <span class="btn-cart"><svg width="14" height="14" viewBox="0 0 24 24"><path fill="#fff" d="M7 18a2 2 0 1 0 0 4 2 2 0 0 0 0-4zm10 0a2 2 0 1 0 0 4 2 2 0 0 0 0-4zM5.2 4H2V2h4.6l1 2H22l-3.5 8H8.1l-1 2H20v2H4l2.3-4.5z"/></svg></span>
    </div>
  </div>
</header>

<nav class="nav">
  <div class="wrap">
    <a href="#">HOME</a><a href="#">ABOUT</a><a href="#">SERVICES ▾</a><a href="#">SHOP</a><a href="#">CONTACT</a>
    <div class="search">Search <svg width="12" height="12" viewBox="0 0 24 24"><circle cx="10" cy="10" r="6" fill="none" stroke="#999" stroke-width="2.5"/><path d="M15 15l6 6" stroke="#999" stroke-width="2.5"/></svg></div>
  </div>
</nav>

<section class="hero" role="img" aria-label="Mechanic working under the hood of a car in a dark workshop">
  <div class="hero-text">
    <h1>LOREMIPSUMIS SIMPLY</h1>
    <h2>Dummy text of the printing</h2>
    <p>Lorem Ipsum is simply dummy text of the printing and typesetting industry. Lorem Ipsum has been the industry's standard dummy text ever since the 1500s.</p>
  </div>
</section>

<section class="partners" aria-label="Partners">
  <span class="partner"></span><span class="partner"></span><span class="partner"></span><span class="partner"></span><span class="partner"></span>
</section>

<section class="intro">
  <div class="wrap">
    <h2 class="sec-title">LOREM IPSUM SIMPLY</h2>
    <p class="sec-lead">Lorem Ipsum is simply dummy text of the printing and typesetting industry. Lorem Ipsum has been the industry's standard dummy text ever since.</p>
    <div class="intro-body">
      <div class="intro-photo" role="img" aria-label="Mechanic in red overalls checking a red car"></div>
      <div class="intro-list">
        <h3>LOREM IPSUM IS SIMPLE</h3>
        <p>Lorem Ipsum is simply dummy text of the printing and typesetting industry. Lorem Ipsum has been the industry's standard dummy text ever since.</p>
        <div class="feature"><span class="badge"><svg width="22" height="22" viewBox="0 0 24 24"><path fill="#fff" d="M5 11l1.5-4.5h11L19 11v7h-2v-2H7v2H5zm2.5-1h9l-1-3h-7z"/></svg></span><div><h4>It was popularised</h4><p>When an unknown printer took a galley of type and scrambled it to make a type specimen book.</p></div></div>
        <div class="feature"><span class="badge"><svg width="22" height="22" viewBox="0 0 24 24"><path fill="#fff" d="M21 6.5l-3.5 3.5-3-3L18 3.5A5 5 0 0 0 12.4 10L3 19.4 4.6 21 14 11.6A5 5 0 0 0 21 6.5z"/></svg></span><div><h4>It was popularised</h4><p>When an unknown printer took a galley of type and scrambled it to make a type specimen book.</p></div></div>
        <div class="feature"><span class="badge"><svg width="22" height="22" viewBox="0 0 24 24"><circle cx="12" cy="12" r="7" fill="none" stroke="#fff" stroke-width="2.5"/><circle cx="12" cy="12" r="2.5" fill="#fff"/></svg></span><div><h4>It was popularised</h4><p>When an unknown printer took a galley of type and scrambled it to make a type specimen book.</p></div></div>
      </div>
    </div>
  </div>
</section>

<section class="services">
  <h2 class="sec-title">SERVICES WE PROVIDE</h2>
  <p class="sec-lead">Lorem Ipsum is simply dummy text of the printing and typesetting industry. Lorem Ipsum has been the industry's standard dummy text.</p>
  <div class="cards">
    <div class="card"><div class="photo" role="img" aria-label="Mechanics inspecting an engine bay" style="background:linear-gradient(135deg,#8b8e93,#4a4c50)"></div><h4>BASIC MAINTENANCE</h4><p>Lorem Ipsum is simply dummy text of the printing and typesetting industry.</p></div>
    <div class="card"><div class="photo" role="img" aria-label="Car being washed with foam" style="background:linear-gradient(135deg,#2f3033,#a8262d 70%,#3b3c40)"></div><h4 class="accent">CAR WASHES</h4><p>Lorem Ipsum is simply dummy text of the printing and typesetting industry.</p></div>
    <div class="card"><div class="photo" role="img" aria-label="Technician aligning a wheel" style="background:linear-gradient(135deg,#e4e4e6,#b52a31 60%,#8c8d90)"></div><h4>ALIGNMENT</h4><p>Lorem Ipsum is simply dummy text of the printing and typesetting industry.</p></div>
  </div>
</section>

<section class="split" role="img" aria-label="Row of parked cars in muted tones">
  <div class="wrap">
    <div>
      <h3>WHAT OUR CLIENTS SAY</h3>
      <div class="quote"><b>Lorem ipsum</b>Lorem Ipsum is simply dummy text of the printing and typesetting industry since the 1500s, when an unknown printer took a galley.<span class="avatar" role="img" aria-label="Client portrait"></span></div>
    </div>
    <div class="form">
      <h3>CONTACT US</h3>
      <div class="form-row"><span class="field">Name</span><span class="field">Email</span></div>
      <div class="form-row"><span class="field">Phone Number</span><span class="field">Subject</span></div>
      <div class="form-row"><span class="field tall">Message</span></div>
      <span class="submit">Submit</span>
    </div>
  </div>
</section>

<section class="about">
  <h2 class="sec-title">LOREM IPSUM SIMPLY</h2>
  <p>Lorem Ipsum is simply dummy text of the printing and typesetting industry. Lorem Ipsum has been the industry's standard dummy text ever since the 1500s, when an unknown printer took a galley of type and scrambled it to make a type specimen book. It has survived not only five centuries, but also the leap into electronic typesetting, remaining essentially unchanged. It was popularised in the 1960s with the release of sheets containing passages, and more recently with desktop publishing software.</p>
  <span class="btn-dark">Read More</span>
</section>

<section class="newsletter">
  <div class="wrap">
    <svg width="46" height="40" viewBox="0 0 46 40"><path d="M2 16L23 2l21 14v22H2z" fill="none" stroke="#fff" stroke-width="3"/><path d="M2 16l21 13 21-13" fill="none" stroke="#fff" stroke-width="3"/></svg>
    <div class="nl-title"><small>SUBSCRIBE</small><strong>OUR NEWSLETTER</strong></div>
    <div class="nl-form"><span class="field">Enter Email Address</span><span class="go">Subscribe</span></div>
  </div>
</section>

<footer class="footer">
  <div class="wrap">
    <div class="f-brand">
      <div class="brand">KTR MOTORHAUS</div>
      <p>Lorem Ipsum is simply dummy text of the printing and typesetting industry. Lorem Ipsum has been the industry's standard dummy text.</p>
      <p>Since the 1500s, when an unknown printer took a galley of type and scrambled it.</p>
    </div>
    <div class="f-col">
      <h4>Lorem Ipsum</h4>
      <ul><li>Lorem ipsum</li><li>is simply</li><li>dummy text of</li><li>the printing</li><li>and</li><li>typesetting</li><li>industry</li></ul>
    </div>
    <div class="f-col f-contact">
      <h4>Contact Us</h4>
      <ul>
        <li><span class="dot"><svg width="8" height="10" viewBox="0 0 8 10"><path d="M4 0a4 4 0 0 0-4 4c0 3 4 6 4 6s4-3 4-6a4 4 0 0 0-4-4z" fill="#222428"/></svg></span>512 NE 9th St Pompano Beach FL 33062</li>
        <li><span class="dot"><svg width="9" height="7" viewBox="0 0 9 7"><rect width="9" height="7" fill="#222428"/></svg></span>rohan@ktrmotorhaus.example</li>
        <li><span class="dot"><svg width="8" height="8" viewBox="0 0 24 24"><path fill="#222428" d="M6.6 10.8a15 15 0 0 0 6.6 6.6l2.2-2.2 5.6 1.8V21A18 18 0 0 1 3 3h4l1.8 5.6z"/></svg></span>954 718 6402</li>
      </ul>
    </div>
  </div>
</footer>
<div class="copy">Copyright © 2019 KTR MOTORHAUS. All Rights Reserved</div>

</body>
</html>
```